IT Company needs full suite of stationery

Our company 4027 Veltrane Partners Inc. is an IT company based in Toronto, Canada. Based on our logo we would like to see business cards(front and back), letterhead, envelope, brochure template. Design would be simple, not too bright, modern but can be used for many years, good theme throughout. Our official logo is the the fullcolor_a, full company name is 4027 Veltrane Partners Inc., Please include full company name on all pieces. Logo can be modified to be the graphic only with the "4027 Partners", I have cropped it myself for a couple files but I am no designer. We will provide lots of feedback so post early and often.
Updates

Reason: Very busy around the holidays, like a lot of the designs currently submitted, will definitely be picking one. Thanks for your submissions and merry Christmas and Happy New Year to everyone.

Industry/Entity Type

Business

```html
<!DOCTYPE html>
<html lang="en">
<head>
<meta charset="utf-8">
<title>4027 Partners – Business Card</title>
<link href="https://fonts.googleapis.com/css2?family=Mulish:wght@400;700;800&display=swap" rel="stylesheet">
<style>
  :root {
    --backdrop: #e4e4e1;
    --card-white: #f7f7f6;
    --card-dark: #3e3e40;
    --green: #3f9c35;
    --green-deep: #1e6b2a;
    --ink: #3a3a3a;
    --ink-soft: #555558;
    --logo-light: #f2f2f2;
  }
  * { box-sizing: border-box; margin: 0; padding: 0; }
  html, body {
    width: 1200px; height: 900px; overflow: hidden;
    background: var(--backdrop);
    font-family: "Mulish", sans-serif;
  }
  .canvas {
    position: relative; width: 1200px; height: 900px;
    display: flex; flex-direction: column; align-items: center; justify-content: center; gap: 56px;
  }
  .card {
    position: relative; width: 560px; height: 320px;
    box-shadow: 0 6px 18px rgba(0,0,0,.18);
    overflow: hidden;
  }

  /* Back */
  .card--back {
    background: var(--card-dark);
    display: flex; align-items: center; justify-content: center;
  }
  .brand { display: flex; align-items: center; gap: 14px; }
  .brand__dot { width: 54px; height: 54px; border-radius: 50%; flex: none; }
  .brand__name { font-weight: 800; letter-spacing: .5px; white-space: nowrap; }
  .card--back .brand__dot { background: var(--logo-light); }
  .card--back .brand__name { color: var(--logo-light); font-size: 40px; }

  /* Front */
  .card--front { background: var(--card-white); }
  .card--front .brand { position: absolute; left: 44px; top: 38px; gap: 10px; }
  .card--front .brand__dot { width: 44px; height: 44px; background: var(--green); }
  .card--front .brand__name { color: var(--green); font-size: 30px; }

  .divider {
    position: absolute; left: 44px; right: 40px; top: 178px;
    height: 1px; background: var(--green);
  }
  .person {
    position: absolute; right: 40px; top: 128px; text-align: right;
  }
  .person__name { font-weight: 800; font-size: 19px; color: var(--ink); letter-spacing: .3px; }
  .person__role { font-size: 14px; color: var(--green); margin-top: 4px; }

  .contacts {
    position: absolute; left: 44px; top: 194px;
    list-style: none; font-size: 12.5px; color: var(--ink-soft); line-height: 20px;
  }
  .contacts li { display: flex; align-items: center; gap: 10px; white-space: nowrap; }
  .contacts svg { width: 12px; height: 12px; fill: var(--green); flex: none; }

  .address {
    position: absolute; right: 40px; top: 194px; text-align: right;
    font-size: 14px; color: var(--ink); line-height: 20px; font-style: normal;
    white-space: nowrap;
  }

  .band {
    position: absolute; left: 0; right: 0; bottom: 0; height: 18px;
    background: linear-gradient(90deg, var(--green-deep), var(--green));
  }
</style>
</head>
<body>
<main class="canvas">
  <section class="card card--back" aria-label="Business card back">
    <div class="brand">
      <span class="brand__dot"></span>
      <span class="brand__name">4027 Partners</span>
    </div>
  </section>

  <section class="card card--front" aria-label="Business card front">
    <div class="brand">
      <span class="brand__dot"></span>
      <span class="brand__name">4027 Partners</span>
    </div>

    <div class="person">
      <p class="person__name">Daniel Kessler</p>
      <p class="person__role">CEO</p>
    </div>

    <div class="divider"></div>

    <ul class="contacts">
      <li>
        <svg viewBox="0 0 24 24" aria-hidden="true"><path d="M6.6 10.8a15.2 15.2 0 0 0 6.6 6.6l2.2-2.2c.3-.3.7-.4 1-.2 1.1.4 2.3.6 3.6.6.6 0 1 .4 1 1V20c0 .6-.4 1-1 1A17 17 0 0 1 3 4c0-.6.4-1 1-1h3.5c.6 0 1 .4 1 1 0 1.3.2 2.5.6 3.6.1.3 0 .7-.2 1z"/></svg>
        +1 416 555 0142
      </li>
      <li>
        <svg viewBox="0 0 24 24" aria-hidden="true"><path d="M6.6 10.8a15.2 15.2 0 0 0 6.6 6.6l2.2-2.2c.3-.3.7-.4 1-.2 1.1.4 2.3.6 3.6.6.6 0 1 .4 1 1V20c0 .6-.4 1-1 1A17 17 0 0 1 3 4c0-.6.4-1 1-1h3.5c.6 0 1 .4 1 1 0 1.3.2 2.5.6 3.6.1.3 0 .7-.2 1z"/></svg>
        +1 416 555 0187
      </li>
      <li>
        <svg viewBox="0 0 24 24" aria-hidden="true"><path d="M2 5h20v14H2zm2 2v.5l8 5 8-5V7zm0 2.9V17h16V9.9l-8 5z"/></svg>
        ceo@veltranepartners.com
      </li>
    </ul>

    <address class="address">
      4027 Veltrane Partners Inc.<br>
      Harbourview Road 118 M5V 2T6<br>
      Toronto, Canada
    </address>

    <div class="band"></div>
  </section>
</main>
</body>
</html>
```